Specialised investor in e-mobility and energy wants business card design

We need a business card design that fits our existing corporate design. <The look and feel must be 'sharp'/'clean', dynamic, communicate momentum, professionalism etc (as one would imagine from a firm in the financial sector). We like the idea of a reverse-side of the card that includes the logo, and the name and contact details on the other. We expect the deliverable to be whatever format might be required to be able to get cards printed directly by a service such as tandor press. Our website is www.orm.capital

```html
<!DOCTYPE html>
<html lang="en">
<head>
<meta charset="UTF-8">
<title>Orm Capital – Business Card</title>
<link href="https://fonts.googleapis.com/css2?family=Poppins:wght@300;400;600&display=swap" rel="stylesheet">
<style>
  :root {
    --backdrop: #c4c4c4;
    --green-light: #8cba4e;
    --green-mid: #5f8f36;
    --green-dark: #2e4d21;
    --ink-green: #2f5224;
    --accent-green: #5c9a2e;
    --paper: #ffffff;
    --ink: #1e1e1e;
  }
  * { margin: 0; padding: 0; box-sizing: border-box; }
  html, body {
    width: 1200px; height: 900px; overflow: hidden;
    background: var(--backdrop);
    font-family: "Poppins", sans-serif;
  }
  .stage { position: relative; width: 1200px; height: 900px; }
  .card {
    position: absolute;
    width: 560px; height: 320px;
    border-radius: 26px;
    overflow: hidden;
    box-shadow: 0 6px 14px rgba(0,0,0,0.25);
  }
  .card--front {
    left: 80px; top: 110px;
    background: linear-gradient(170deg, var(--green-light) 0%, var(--green-mid) 45%, var(--green-dark) 100%);
    display: flex; align-items: center; justify-content: center;
  }
  .brand-name {
    font-weight: 300;
    font-size: 58px;
    letter-spacing: 1px;
    display: flex; align-items: center; gap: 16px;
    white-space: nowrap;
  }
  .brand-dot { width: 16px; height: 16px; border-radius: 50%; }
  .card--front .brand-name { color: var(--paper); }
  .card--front .brand-dot { background: var(--paper); }

  .card--back { left: 560px; top: 470px; background: var(--paper); }
  .card--back .brand-name {
    position: absolute; left: 40px; top: 62px;
    color: var(--ink-green); font-size: 50px;
  }
  .card--back .brand-dot { background: var(--ink-green); width: 14px; height: 14px; }

  .contact { position: absolute; left: 40px; bottom: 34px; color: var(--ink); }
  .contact__name {
    font-weight: 600; font-size: 22px; color: var(--ink-green);
    letter-spacing: 0.5px; line-height: 1.1;
  }
  .contact__role { font-size: 15px; margin-bottom: 12px; }
  .contact__line {
    display: flex; align-items: center; gap: 8px;
    font-size: 15px; line-height: 1.45; white-space: nowrap;
  }
  .contact__line svg { width: 14px; height: 14px; flex: none; }
  .contact__web .accent { color: var(--accent-green); }

  .address {
    position: absolute; right: 34px; bottom: 70px;
    text-align: right; font-size: 13.5px; line-height: 1.35; color: var(--ink);
    font-style: normal; white-space: nowrap;
  }
</style>
</head>
<body>
<main class="stage">
  <section class="card card--front" aria-label="Card front">
    <div class="brand-name"><span class="brand-dot"></span>Orm Capital</div>
  </section>

  <section class="card card--back" aria-label="Card back">
    <div class="brand-name"><span class="brand-dot"></span>Orm Capital</div>

    <div class="contact">
      <p class="contact__name">DANIEL HARPER</p>
      <p class="contact__role">Managing Director</p>
      <p class="contact__line">
        <svg viewBox="0 0 16 16" aria-hidden="true"><path d="M4 1.5l2.2 3-1.4 1.6c.9 2 2.4 3.5 4.4 4.4l1.6-1.4 3 2.2-1.2 2.7C6.8 13.8 2.2 9.2 1.3 3z" fill="var(--ink-green)"/></svg>
        <span>031-555 204 617</span>
      </p>
      <p class="contact__line">
        <svg viewBox="0 0 16 16" aria-hidden="true"><rect x="1" y="3" width="14" height="10" fill="var(--ink-green)"/><path d="M1 3l7 6 7-6" stroke="#fff" stroke-width="1.3" fill="none"/></svg>
        <span>hello@ormmail.com</span>
      </p>
      <p class="contact__line contact__web">
        <svg viewBox="0 0 16 16" aria-hidden="true"><g fill="none" stroke="var(--ink-green)" stroke-width="1.4"><circle cx="8" cy="8" r="6.5"/><ellipse cx="8" cy="8" rx="2.8" ry="6.5"/><path d="M1.5 8h13M2.5 4.8h11M2.5 11.2h11"/></g></svg>
        <span>www.<span class="accent">orm</span>.capital</span>
      </p>
    </div>

    <address class="address">
      87, Linden Quay Road, Suite 4<br>
      30418, Westmark
    </address>
  </section>
</main>
</body>
</html>
```